Brellick Commercial Roof Restoration LLC needs billboard and banner designs

Need billboard ad design for small commercial roof restoration company. Looking for a billboard design that can be used on digital and hard print billboards. Also need banner design for 4' x 8' job site banners that will go by roadside to draw potential customers to our brand. Our vision for bill board would show an attractive women in business dress, clearly in a building having to use an (red) umbrella (inside building) due to leaking roof. Caption "WE CAN HELP" www.BRELLICKCOMMERCIALROOF.example
For banner design we would use some before/after roof photos (attached, blend/overlay at an angle) in background with "Another Quality Commercial Roof Restoration By:" "Brellick Commercial Roof LLC" "Is your commercial roof leaking? Call 555.318.4726 for help".
All final designs should communicate commercial roof restoration only.
Target Market(s)
Commercial building owner/managers
Industry/Entity Type
Roofing
Font styles to use
Requirements
Must have
- Just added a Jpeg file of a logo of the company that we buy our products from. This logo & "Certified Premier Installers" needs to be added to the project. It only needs to have a small footprint on the ad. Contact me if you have questions. Thank you.
Nice to have
- Billboard design; our name, website, relay our message with image. As described above in project description
Banner; Our name, phone number and bold written message

```html
<!DOCTYPE html>
<html lang="en">
<head>
<meta charset="utf-8">
<title>Brellick Commercial Roof Restoration – Billboard</title>
<link rel="stylesheet" href="https://fonts.googleapis.com/css2?family=Montserrat:wght@400;700;800&display=swap">
<style>
  :root {
    --page: #ffffff;
    --brand-blue: #2a69ab;
    --brand-red: #c4211f;
    --ink: #231f20;
    --white: #ffffff;
    --photo-light: #e9e6e0;
    --photo-mid: #8a8f9c;
    --photo-accent: #d9232a;
    --photo-dark: #2b2d36;
  }
  * { box-sizing: border-box; margin: 0; padding: 0; }
  html, body {
    width: 897px; height: 1200px; overflow: hidden;
    background: var(--page);
  }
  .canvas {
    position: relative; width: 897px; height: 1200px;
    background: var(--page);
  }
  .billboard {
    position: absolute; left: 48px; top: 400px;
    width: 800px; height: 400px;
    background: var(--white);
    box-shadow: 0 3px 6px rgba(0,0,0,0.25);
    overflow: hidden;
    font-family: "Montserrat", sans-serif;
  }
  .billboard-shapes { position: absolute; inset: 0; }
  .copy {
    position: absolute; left: 410px; width: 390px;
    text-align: center; white-space: nowrap;
  }
  .brand-name {
    top: 30px; color: var(--brand-blue); font-weight: 800;
    line-height: 1.05;
  }
  .brand-name .name-main { display: block; font-size: 44px; letter-spacing: 2px; }
  .brand-name .name-sub { display: block; font-size: 15px; letter-spacing: 0.5px; margin-top: 4px; }
  .headline-lead {
    top: 158px; color: var(--ink); font-weight: 400;
    font-size: 26px; letter-spacing: 0.5px;
  }
  .headline {
    top: 186px; color: var(--brand-blue); font-weight: 700;
    font-size: 62px; line-height: 1; letter-spacing: 0.5px;
  }
  .offer {
    top: 257px; color: var(--white); font-size: 36px;
    font-weight: 400; line-height: 1; letter-spacing: 1px;
  }
  .offer strong { font-weight: 700; }
  .phone {
    top: 295px; color: var(--white); font-size: 32px;
    font-weight: 700; line-height: 1; letter-spacing: 1px;
  }
  .website {
    position: absolute; left: 0; right: 0; top: 337px; height: 63px;
    display: flex; align-items: center; justify-content: center;
    color: var(--white); font-weight: 700; font-size: 30px;
    letter-spacing: 0.3px;
  }
</style>
</head>
<body>
  <main class="canvas">
    <section class="billboard">
      <svg class="billboard-shapes" viewBox="0 0 800 400" width="800" height="400">
        <defs>
          <linearGradient id="photo-tones" x1="0" y1="0" x2="1" y2="1">
            <stop offset="0" stop-color="var(--photo-light)"/>
            <stop offset="0.45" stop-color="var(--photo-mid)"/>
            <stop offset="0.7" stop-color="var(--photo-accent)"/>
            <stop offset="1" stop-color="var(--photo-dark)"/>
          </linearGradient>
        </defs>
        <path class="offer-band" d="M348 251 H800 V330 H334 Z" fill="var(--brand-red)"/>
        <rect class="web-band" x="0" y="337" width="800" height="63" fill="var(--brand-blue)"/>
        <path class="hero-photo" role="img"
              aria-label="Photo: businesswoman in black holding a red umbrella indoors beneath a water-stained leaking ceiling"
              d="M0 0 H310 C420 55 450 190 345 251 L332 330 H0 Z"
              fill="url(#photo-tones)"/>
      </svg>

      <div class="copy brand-name">
        <span class="name-main">BRELLICK</span>
        <span class="name-sub">COMMERCIAL ROOF RESTORATION</span>
      </div>
      <div class="copy headline-lead">COMMERCIAL ROOF</div>
      <div class="copy headline">LEAKING?</div>
      <div class="copy offer">WE CAN <strong>HELP</strong></div>
      <div class="copy phone">555.318.4726</div>
      <div class="website">www.BRELLICKCOMMERCIALROOF.example</div>
    </section>
  </main>
</body>
</html>
```